landing and results page for local search engine for childrens stuff

wimbro.it is local search engine to find children clothes, bikes, toys, etc locally.

we search thousands of sites tradlo, swapnest and many more to bring together millions of ads so you can find them all in one place, and organize them with useful features so parents can find local bargains for kids stuff.

the key here is we specialise in finding kids gear, and only bring you results that are local to the user.
look and feel something like this http://www.plinvo.com/
and http://www.tesk.com/

Target Market(s)

mums, parents , people with kids

Industry/Entity Type

Tradlo

Requirements
Must have
• it must convey that this is a location aware search engine for kids stuff. an image similar to this http://www.brambolapp.com/
on landing page

```html
<!DOCTYPE html>
<html lang="en">
<head>
<meta charset="utf-8">
<title>wimbro.it — local search for kids stuff</title>
<link rel="stylesheet" href="https://fonts.googleapis.com/css2?family=Questrial&family=Michroma&family=Kaushan+Script&family=Arimo:wght@400&display=swap">
<style>
  :root {
    --gold: #c59a5e;
    --header-bg: #e8e9ef;
    --ink-dark: #27303c;
    --hero-bg: #dde3e9;
    --hero-title: #1f3f66;
    --hero-text: #3b6ca3;
    --panel-bg: #232b36;
    --panel-rule: #3a4552;
    --label-muted: #a9b3c1;
    --field-top: #8596ae;
    --field-bottom: #74869f;
    --field-text: #2b3440;
    --btn-top: #e6c48f;
    --btn-bottom: #a97a3e;
    --btn-text: #4a3216;
  }
  * { box-sizing: border-box; margin: 0; padding: 0; }
  html, body { width: 1200px; height: 674px; overflow: hidden; background: var(--header-bg); }
  .page { position: relative; width: 1200px; height: 674px; overflow: hidden; font-family: "Arimo", Arial, sans-serif; }

  .top-rule { position: absolute; left: 0; top: 0; width: 1200px; height: 7px; background: var(--gold); }
  .top-notch { position: absolute; left: 569px; top: 6px; }

  .site-header { position: absolute; left: 0; top: 7px; width: 1200px; height: 90px; background: var(--header-bg); border-bottom: 1px solid #c9ccd3; }
  .brand { position: absolute; left: 70px; top: 24px; font-family: "Questrial", sans-serif; font-size: 34px; color: var(--ink-dark); text-transform: uppercase; letter-spacing: 1px; }
  .main-nav { position: absolute; right: 50px; top: 26px; display: flex; font-family: "Questrial", sans-serif; font-size: 17px; color: var(--ink-dark); }
  .main-nav a { color: inherit; text-decoration: none; }
  .main-nav .sep { margin: 0 17px; }

  .hero { position: absolute; left: 0; top: 98px; width: 1200px; height: 360px; background: radial-gradient(ellipse at 70% 40%, #eef1f4 0%, var(--hero-bg) 70%, #d3dae2 100%); }
  .hero-visual { position: absolute; left: 60px; top: 38px; width: 460px; height: 322px; background: linear-gradient(160deg, #c9a27a 0%, #d8d2cc 35%, #a5212f 65%, #7e1622 100%); border-radius: 4px 4px 0 0; }
  .hero-title { position: absolute; left: 550px; top: 76px; width: 540px; text-align: center; font-family: "Michroma", sans-serif; font-variant: small-caps; font-size: 19px; color: var(--hero-title); letter-spacing: 1px; }
  .hero-text { position: absolute; left: 560px; top: 137px; width: 525px; text-align: center; font-size: 14px; line-height: 25px; color: var(--hero-text); }
  .social { position: absolute; left: 988px; top: 297px; display: flex; gap: 6px; }
  .social span { display: block; width: 30px; height: 30px; border-radius: 3px; }
  .social .s1 { background: #3a5a98; }
  .social .s2 { background: #5fb6d6; }
  .social .s3 { background: #1b3f8a; }
  .social .s4 { background: #c9ccd2; }

  .search-panel { position: absolute; left: 0; top: 457px; width: 1200px; height: 217px; background: var(--panel-bg); border-top: 1px solid #1a212a; }
  .search-panel::before { content: ""; position: absolute; left: 0; right: 0; top: 8px; border-top: 1px dashed var(--panel-rule); }
  .search-group { position: absolute; top: 36px; width: 346px; }
  .group-what { left: 63px; }
  .group-where { left: 426px; }
  .group-priority { left: 788px; }
  .search-label { font-size: 20px; color: var(--label-muted); padding-left: 5px; height: 32px; }
  .search-label em { font-family: "Kaushan Script", cursive; font-style: normal; color: #ffffff; font-size: 21px; }
  .select-field { position: relative; margin-top: 13px; height: 53px; background: linear-gradient(var(--field-top), var(--field-bottom)); box-shadow: inset 0 0 10px rgba(20,30,45,.45); font-size: 14px; color: var(--field-text); line-height: 53px; padding-left: 20px; }
  .select-field::after { content: ""; position: absolute; right: 46px; top: 8px; bottom: 8px; border-left: 1px solid #b9c5d4; }
  .select-field svg { position: absolute; right: 10px; top: 15px; }
  .search-actions { position: absolute; right: 67px; top: 155px; display: flex; gap: 10px; }
  .btn { height: 42px; border: 1px solid #f2dcb3; border-radius: 4px; background: linear-gradient(var(--btn-top), var(--btn-bottom)); font-size: 16px; color: var(--btn-text); font-family: "Arimo", Arial, sans-serif; }
  .btn-advanced { width: 168px; }
  .btn-search { width: 120px; }
</style>
</head>
<body>
<div class="page">
  <div class="top-rule"></div>
  <svg class="top-notch" width="24" height="12" viewBox="0 0 24 12"><polygon points="0,0 24,0 12,12" fill="#c59a5e"/></svg>

  <header class="site-header">
    <div class="brand">wimbro.it</div>
    <nav class="main-nav">
      <a href="#">HOME</a><span class="sep">/</span>
      <a href="#">About Us</a><span class="sep">/</span>
      <a href="#">Advanced Search</a><span class="sep">/</span>
      <a href="#">Our Products</a><span class="sep">/</span>
      <a href="#">Contacts</a>
    </nav>
  </header>

  <section class="hero">
    <div class="hero-visual" role="img" aria-label="Open red gift box overflowing with kids toys: teddy bear, football, doll and toy cars"></div>
    <h1 class="hero-title">The standard Lorem Ipsum passage</h1>
    <p class="hero-text">Lorem ipsum dolor sit amet, consectetur adipisicing elit, sed do eiusmod tempor incididunt ut labore et dolore magna aliqua. Ut enim ad minim veniam, quis nostrud exercitation ullamco laboris nisi ut aliquip ex ea commodo consequat.</p>
    <div class="social" aria-label="Social links">
      <span class="s1"></span><span class="s2"></span><span class="s3"></span><span class="s4"></span>
    </div>
  </section>

  <section class="search-panel">
    <div class="search-group group-what">
      <div class="search-label"><em>What</em> you would like to search?</div>
      <div class="select-field">Category or Keyword....
        <svg width="26" height="24" viewBox="0 0 26 24"><polygon points="0,0 26,0 13,24" fill="#ffffff"/></svg>
      </div>
    </div>
    <div class="search-group group-where">
      <div class="search-label"><em>Search</em> by location?</div>
      <div class="select-field">Add your Location....
        <svg width="26" height="24" viewBox="0 0 26 24"><polygon points="0,0 26,0 13,24" fill="#ffffff"/></svg>
      </div>
    </div>
    <div class="search-group group-priority">
      <div class="search-label"><em>Search</em> by priority?</div>
      <div class="select-field">All Type
        <svg width="26" height="24" viewBox="0 0 26 24"><polygon points="0,0 26,0 13,24" fill="#ffffff"/></svg>
      </div>
    </div>
    <div class="search-actions">
      <button class="btn btn-advanced">Advanced Search</button>
      <button class="btn btn-search">Search</button>
    </div>
  </section>
</div>
</body>
</html>
```